Quilvo Garage Doors Business Card

I need a Business Card for my garage door business:
Quilvo Garage Doors.
please add:
logo
phone number: 855-3-QUILVO
(853-392)

email: service@quilvogaragedoors.com
website: www.quilvogaragedoors.com

The attached image is recommendation ONLY.

```html
<!DOCTYPE html>
<html lang="en">
<head>
<meta charset="utf-8">
<title>Quilvo Garage Doors – Business Card</title>
<link href="https://fonts.googleapis.com/css2?family=Open+Sans:wght@400;600;700&display=swap" rel="stylesheet">
<style>
  :root {
    --page: #e6e4e2;
    --card: #121212;
    --card-edge: #1c1c1c;
    --teal: #3fb8c4;
    --white: #f2f2f2;
    --soft: #c9c9c9;
    --divider: #6a6a6a;
  }
  * { margin: 0; padding: 0; box-sizing: border-box; }
  html, body {
    width: 1200px; height: 814px; overflow: hidden;
    background: var(--page);
    font-family: "Open Sans", Arial, sans-serif;
  }
  .sheet {
    position: relative; width: 1200px; height: 814px;
    display: flex; align-items: center; justify-content: center; gap: 60px;
  }
  .card {
    position: relative; width: 520px; height: 297px;
    background: var(--card);
    border: 1px solid var(--card-edge);
    box-shadow: 0 6px 18px rgba(0,0,0,.25);
  }
  /* front */
  .brand {
    position: absolute; left: 36px; top: 160px;
    display: flex; align-items: center; gap: 14px;
  }
  .brand-mark { width: 50px; height: 50px; background: var(--teal); border-radius: 6px; }
  .brand-name {
    color: var(--white); font-weight: 600; font-size: 21px; line-height: 1.15;
  }
  .divider {
    position: absolute; left: 252px; top: 78px; width: 1px; height: 170px;
    background: var(--divider);
  }
  .contact { position: absolute; left: 268px; top: 76px; color: var(--white); }
  .person-name { color: var(--teal); font-size: 19px; font-weight: 600; line-height: 1.2; }
  .person-title { font-size: 12.5px; margin-bottom: 8px; }
  .contact-line {
    display: flex; align-items: center; gap: 7px;
    font-size: 12.5px; line-height: 19px;
  }
  .contact-line svg { width: 12px; height: 12px; flex: none; fill: var(--teal); }
  .contact-line.indent { padding-left: 19px; }
  /* back */
  .back-brand {
    position: absolute; left: 0; right: 0; top: 100px;
    display: flex; align-items: center; justify-content: center; gap: 12px;
  }
  .back-mark { width: 40px; height: 40px; background: var(--soft); border-radius: 5px; }
  .back-name { color: var(--soft); font-weight: 600; font-size: 24px; }
  .back-web {
    position: absolute; left: 0; right: 0; top: 200px; text-align: center;
    color: var(--soft); font-size: 13px; letter-spacing: .5px;
  }
</style>
</head>
<body>
<main class="sheet">
  <section class="card card-front">
    <div class="brand">
      <div class="brand-mark"></div>
      <div class="brand-name">Quilvo<br>Garage Doors</div>
    </div>
    <div class="divider"></div>
    <div class="contact">
      <div class="person-name">Dara Lenox</div>
      <div class="person-title">CEO/Founder</div>
      <div class="contact-line">
        <svg viewBox="0 0 24 24"><path d="M6.6 10.8a15 15 0 0 0 6.6 6.6l2.2-2.2c.3-.3.7-.4 1-.2 1.1.4 2.3.6 3.6.6.6 0 1 .4 1 1V20c0 .6-.4 1-1 1A17 17 0 0 1 3 4c0-.6.4-1 1-1h3.5c.6 0 1 .4 1 1 0 1.3.2 2.5.6 3.6.1.3 0 .7-.2 1z"/></svg>
        <span>855-3-QUILVO</span>
      </div>
      <div class="contact-line indent"><span>(853-392)</span></div>
      <div class="contact-line">
        <svg viewBox="0 0 24 24"><path d="M2 5h20v14H2zm2 2v.5l8 5 8-5V7zm0 2.8V17h16V9.8l-8 5z"/></svg>
        <span>service@quilvogaragedoors.com</span>
      </div>
      <div class="contact-line">
        <svg viewBox="0 0 24 24"><circle cx="12" cy="12" r="10"/></svg>
        <span>www.quilvogaragedoors.com</span>
      </div>
    </div>
  </section>
  <section class="card card-back">
    <div class="back-brand">
      <div class="back-mark"></div>
      <div class="back-name">Quilvo Garage Doors</div>
    </div>
    <div class="back-web">www.quilvogaragedoors.com</div>
  </section>
</main>
</body>
</html>
```